BRIM Outreach Partners Business Card Rebrand

Hello Designers! We are looking for help designing our new business card to go in conjunction with our company rebrand. Unfortunately, we have an event mid June that requires we get these printed ASAP (before our new website is launched.) We have a mostly complete Brand Book which I have uploaded to this request for your reference to company information, style, fonts. I've also enclosed our logo file in .eps & .jpg. Attached is a sample business card my boss liked but said was "too simple." I made it in Canva and do not profess to be a designer. NOT FOR DESIGN REFERENCE, ONLY FOR CONTEXT Here is what our old website looks like: https://brimoutreachpartners.com/.

```html
<!DOCTYPE html>
<html lang="en">
<head>
<meta charset="utf-8">
<title>BRIM Outreach Partners – Business Card</title>
<link rel="stylesheet" href="https://fonts.googleapis.com/css2?family=Fira+Sans:wght@400;600;700&display=swap">
<style>
  :root {
    --backdrop: #8f8f8f;
    --card-white: #ffffff;
    --card-black: #000000;
    --ink: #1a1a1a;
    --brand-blue: #4db3e6;
    --mark-grey: #dcdcdc;
  }
  * { margin: 0; padding: 0; box-sizing: border-box; }
  html, body {
    width: 1200px;
    height: 1200px;
    overflow: hidden;
    background: var(--backdrop);
    font-family: "Fira Sans", sans-serif;
  }
  .card {
    position: absolute;
    left: 281px;
    width: 641px;
    height: 365px;
    border-radius: 40px;
    overflow: hidden;
  }
  .card--front { top: 195px; background: var(--card-white); color: var(--ink); }
  .card--back  { top: 639px; background: var(--card-black); }

  .person { position: absolute; left: 52px; top: 104px; }
  .person__name {
    font-size: 28px;
    font-weight: 700;
    letter-spacing: 0.2px;
    line-height: 1;
    text-transform: uppercase;
  }
  .person__title {
    margin-top: 8px;
    font-size: 16px;
    font-weight: 400;
  }
  .contact-list { list-style: none; margin-top: 14px; }
  .contact-list li {
    display: flex;
    align-items: center;
    height: 22.5px;
    font-size: 15px;
    letter-spacing: 0.3px;
  }
  .contact-list svg { width: 12px; height: 12px; margin-right: 8px; fill: var(--ink); flex: none; }

  .front-brand {
    position: absolute;
    left: 410px;
    top: 102px;
    width: 160px;
    text-align: center;
  }
  .front-brand__dot {
    width: 96px; height: 96px;
    border-radius: 50%;
    background: var(--brand-blue);
    margin: 0 auto 12px;
  }
  .front-brand__name {
    font-size: 16px;
    font-weight: 600;
    color: var(--brand-blue);
    line-height: 1.2;
  }

  .back-brand {
    position: absolute;
    left: 120px;
    top: 114px;
    display: flex;
    align-items: center;
  }
  .back-brand__dot {
    width: 138px; height: 138px;
    border-radius: 50%;
    background: var(--brand-blue);
    margin-right: 40px;
  }
  .back-brand__name {
    color: var(--mark-grey);
    font-weight: 600;
    line-height: 1;
  }
  .back-brand__name .lead { display: block; font-size: 108px; letter-spacing: -2px; }
  .back-brand__name .tail { display: block; font-size: 25px; margin-top: 4px; letter-spacing: -0.3px; }
</style>
</head>
<body>

<section class="card card--front" aria-label="Card front">
  <div class="person">
    <h1 class="person__name">Marcus Dell-Whitford</h1>
    <p class="person__title">Managing Partner</p>
    <ul class="contact-list">
      <li>
        <svg viewBox="0 0 12 12" aria-hidden="true"><path d="M3 0h6a1 1 0 0 1 1 1v10a1 1 0 0 1-1 1H3a1 1 0 0 1-1-1V1a1 1 0 0 1 1-1zm.4 1.4v8h5.2v-8zM6 10a.6.6 0 1 0 0 1.2A.6.6 0 0 0 6 10z"/></svg>
        +395-555-0147
      </li>
      <li>
        <svg viewBox="0 0 12 12" aria-hidden="true"><path d="M0 2.5h12v7H0zM.8 3.2 6 6.8l5.2-3.6v-.1H.8z"/></svg>
        marcus@brimoutreachpartners.com
      </li>
      <li>
        <svg viewBox="0 0 12 12" aria-hidden="true"><path d="M6 0a6 6 0 1 0 0 12A6 6 0 0 0 6 0zm-1 2.2 1.6.6.2 1.4-1.4 1.2L3.6 5 2.6 3.6A4.6 4.6 0 0 1 5 2.2zm2 5.6 2.2.2-.8 2a4.6 4.6 0 0 1-2 .9L6.6 9z"/></svg>
        www.brimoutreachpartners.com
      </li>
      <li>
        <svg viewBox="0 0 12 12" aria-hidden="true"><path d="M6 0a4 4 0 0 1 4 4c0 3-4 8-4 8S2 7 2 4a4 4 0 0 1 4-4zm0 2.4a1.6 1.6 0 1 0 0 3.2 1.6 1.6 0 0 0 0-3.2z"/></svg>
        Dayton, OH Based (Eastern Time)
      </li>
    </ul>
  </div>

  <div class="front-brand">
    <div class="front-brand__dot"></div>
    <p class="front-brand__name">BRIM Outreach Partners</p>
  </div>
</section>

<section class="card card--back" aria-label="Card back">
  <div class="back-brand">
    <div class="back-brand__dot"></div>
    <p class="back-brand__name"><span class="lead">BRIM</span><span class="tail">OUTREACH PARTNERS</span></p>
  </div>
</section>

</body>
</html>
```